General Contractors need a new Crisp updated Card Design

We need a new business card design for our company of 25 years based in Toronto call Holvaster Building Inc. : Our goal is to be the leading commercial contractors in Toronto by providing exceptional value to our clients. We work very hard to deliver professional, quality, service in conjunction with consistent price competitiveness to all of our clients on every single project.

Target Market(s)

Design & Build Clients

Industry/Entity Type

Construction Company

Contact Information for Business Card

Address:
18 North Tamlin Glen Road, Unit 57, Marbrook Vale, ON, K7T 2R9
Office: 905-218-5937

Holvasters Logo
Employee Job Description
Employee Cell Phone #
Employee Email
www.holvaster-example.com

Colors

Designer to choose colors to be used in the design.

Requirements
Must have
• Quote Company Saying:
• "Professional. Quality. Service."
Nice to have
• New Crisp up to date look. simple & fresh ( Not to Busy)
Should not have
• NO BLUE PRINTS ON THE BUSINESS CARDS

```html
<!DOCTYPE html>
<html lang="en">
<head>
<meta charset="utf-8">
<title>Holvaster Building Inc. – Business Card</title>
<link rel="stylesheet" href="https://fonts.googleapis.com/css2?family=Fira+Sans:wght@400;500&family=Libre+Baskerville&display=swap">
<style>
  :root {
    --brand-green: #00705f;
    --pale-green: #b3cdc3;
    --paper: #ffffff;
    --backdrop: #e4e4e2;
  }
  * { margin: 0; padding: 0; box-sizing: border-box; }
  html, body { width: 1154px; height: 1200px; overflow: hidden; }
  body {
    background: var(--backdrop);
    font-family: "Fira Sans", Arial, sans-serif;
    position: relative;
  }
  .card {
    position: absolute;
    left: 156px;
    width: 842px;
    height: 481px;
    background: var(--brand-green);
    overflow: hidden;
  }
  .card--front { top: 91px; }
  .card--back  { top: 634px; }

  .edge-band { position: absolute; }
  .edge-band--white { background: var(--paper); }
  .edge-band--pale  { background: var(--pale-green); }

  /* Front */
  .front-panel {
    position: absolute;
    left: 35px; top: 35px; right: 35px; bottom: 36px;
    background: var(--paper);
  }
  .front-wordmark {
    position: absolute;
    left: 0; right: 0; top: 150px;
    display: flex; justify-content: center; align-items: center; gap: 18px;
  }
  .wordmark-square {
    width: 58px; height: 58px;
    background: var(--brand-green);
  }
  .wordmark-name {
    font-weight: 500;
    font-size: 38px;
    letter-spacing: 1px;
    color: var(--brand-green);
  }
  .tagline {
    position: absolute;
    left: 0; right: 0; top: 362px;
    text-align: center;
    font-weight: 500;
    font-size: 29px;
    letter-spacing: 0.3px;
    color: var(--brand-green);
  }
  .bottom-tab {
    position: absolute;
    left: 363px; bottom: 3px;
    width: 116px; height: 26px;
    background: var(--pale-green);
  }

  /* Back */
  .back-header {
    position: absolute;
    left: 0; right: 0; top: 43px; height: 105px;
    background: var(--paper);
    display: flex; justify-content: center; align-items: center; gap: 16px;
  }
  .back-header .wordmark-square { width: 50px; height: 50px; }
  .back-header .wordmark-name { font-size: 34px; }
  .back-frame {
    position: absolute;
    left: 36px; top: 33px;
    width: 774px; height: 416px;
    border: 3px solid var(--paper);
  }
  .employee-name {
    position: absolute;
    left: 65px; top: 183px;
    font-family: "Libre Baskerville", Georgia, serif;
    font-size: 34px;
    color: var(--paper);
  }
  .employee-role {
    position: absolute;
    left: 65px; top: 229px;
    font-size: 19px;
    color: var(--paper);
  }
  .contact-list {
    position: absolute;
    right: 64px; top: 228px;
    text-align: right;
    color: var(--paper);
    list-style: none;
  }
  .contact-list li { font-size: 19px; line-height: 30px; }
  .contact-list .contact-gap { height: 30px; }
  .contact-list .contact-web { font-size: 17px; line-height: 27px; }
  .address {
    position: absolute;
    left: 65px; right: 64px; top: 405px;
    text-align: right;
    font-size: 19px;
    color: var(--paper);
    letter-spacing: 0.2px;
  }
</style>
</head>
<body>

<section class="card card--front" aria-label="Business card front">
  <div class="edge-band edge-band--white" style="left:0;top:190px;width:35px;height:42px"></div>
  <div class="edge-band edge-band--pale"  style="left:0;top:246px;width:35px;height:42px"></div>
  <div class="edge-band edge-band--white" style="right:0;top:190px;width:35px;height:42px"></div>
  <div class="edge-band edge-band--pale"  style="right:0;top:246px;width:35px;height:42px"></div>
  <div class="front-panel">
    <div class="front-wordmark">
      <span class="wordmark-square"></span>
      <span class="wordmark-name">HOLVASTER BUILDING INC.</span>
    </div>
    <p class="tagline">PROFESSIONAL • QUALITY • SERVICE</p>
  </div>
  <div class="bottom-tab"></div>
</section>

<section class="card card--back" aria-label="Business card back">
  <div class="back-header">
    <span class="wordmark-square"></span>
    <span class="wordmark-name">HOLVASTER BUILDING INC.</span>
  </div>
  <div class="edge-band edge-band--white" style="left:0;top:176px;width:36px;height:42px"></div>
  <div class="edge-band edge-band--pale"  style="left:0;top:232px;width:36px;height:42px"></div>
  <div class="edge-band edge-band--white" style="right:0;top:176px;width:36px;height:42px"></div>
  <div class="edge-band edge-band--pale"  style="right:0;top:232px;width:36px;height:42px"></div>
  <div class="back-frame"></div>
  <h1 class="employee-name">EMPLOYEE NAME</h1>
  <p class="employee-role">POSITION</p>
  <ul class="contact-list">
    <li>T (905) 218-5937</li>
    <li>M (000) 000-0000</li>
    <li class="contact-gap"></li>
    <li class="contact-web">NAME@HOLVASTER-EXAMPLE.COM</li>
    <li class="contact-web">WWW.HOLVASTER-EXAMPLE.COM</li>
  </ul>
  <p class="address">18 NORTH TAMLIN GLEN ROAD, UNIT 57 | MARBROOK VALE | ONTARIO | K7T 2R9</p>
  <div class="bottom-tab"></div>
</section>

</body>
</html>
```